Roofing Contractor business card redesign

I want to redesign my business card with a fresh, eye catching concept

Target Market(s)

Residential Roofing Clients, potential employees, and subcontractors.

Industry/Entity Type

Business

Colors

Designer to choose colors to be used in the design.

Requirements
Nice to have
• I just want something that's more pleasing to the eye. You can use a combination of either / or of my logos.

```html
<!DOCTYPE html>
<html lang="en">
<head>
<meta charset="utf-8">
<title>Fair Deal Builders – Business Card</title>
<link href="https://fonts.googleapis.com/css2?family=Anton&family=Oswald:wght@500;700&family=Open+Sans:wght@600;700&display=swap" rel="stylesheet">
<style>
  :root {
    --backdrop: #2b2b2b;
    --card-orange: #e8792c;
    --band-brown: #3a1f1a;
    --ink-brown: #3b211b;
    --accent-yellow: #ffd23a;
    --rule-white: #fbeee2;
    --art-cream: #f4e6c8;
    --art-orange: #d9672a;
  }
  * { box-sizing: border-box; margin: 0; padding: 0; }
  html, body { width: 1200px; height: 660px; overflow: hidden; }
  body {
    background: var(--backdrop);
    display: flex;
    align-items: center;
    justify-content: center;
    gap: 48px;
    font-family: "Open Sans", sans-serif;
  }
  .card {
    position: relative;
    width: 520px;
    height: 297px;
    background: var(--card-orange);
    overflow: hidden;
    box-shadow: 0 12px 28px rgba(0,0,0,.5);
  }
  .band {
    position: absolute;
    left: 0; right: 0;
    height: 22px;
    background: var(--band-brown);
  }
  .band--top { top: 0; border-bottom: 2px solid var(--rule-white); }
  .band--bottom { bottom: 0; border-top: 2px solid var(--rule-white); }

  /* Front */
  .front-logo {
    position: absolute;
    inset: 22px 0;
    display: flex;
    flex-direction: column;
    align-items: center;
    justify-content: center;
    color: var(--ink-brown);
    font-family: "Oswald", sans-serif;
    font-weight: 700;
  }
  .front-logo__row { display: flex; align-items: center; gap: 14px; }
  .front-logo__name { font-size: 62px; line-height: 1; letter-spacing: 1px; }
  .front-logo__dot {
    width: 54px; height: 54px; border-radius: 50%;
    background: var(--ink-brown);
  }
  .front-logo__sub { font-size: 30px; line-height: 1.2; margin-top: 4px; }

  /* Back */
  .back-art {
    position: absolute;
    left: 26px; top: 52px;
    width: 200px; height: 200px;
    border-radius: 50%;
    border: 8px solid var(--ink-brown);
    background: radial-gradient(circle at 50% 40%, var(--art-cream) 0 45%, var(--art-orange) 46% 100%);
  }
  .back-info {
    position: absolute;
    right: 22px; top: 32px;
    text-align: right;
    color: var(--ink-brown);
  }
  .back-info__brand {
    font-family: "Oswald", sans-serif; font-weight: 700;
    font-size: 30px; line-height: 1;
  }
  .back-info__brand-sub {
    font-family: "Oswald", sans-serif; font-weight: 700;
    font-size: 13px; margin-bottom: 8px;
  }
  .back-info__person {
    font-family: "Anton", sans-serif;
    font-size: 20px; letter-spacing: 1px;
  }
  .back-info__title {
    color: var(--accent-yellow);
    font-weight: 700; font-size: 12px; line-height: 1.35;
  }
  .contact-list { list-style: none; margin-top: 10px; font-weight: 700; font-size: 12px; line-height: 1.5; }
  .contact-list li { display: flex; justify-content: flex-end; align-items: center; gap: 6px; }
  .contact-list svg { width: 11px; height: 11px; fill: var(--accent-yellow); }
  .contact-list .no-icon { padding-right: 17px; }
</style>
</head>
<body>
  <section class="card card--front">
    <div class="band band--top"></div>
    <div class="front-logo">
      <div class="front-logo__row">
        <span class="front-logo__name">Fair Deal</span>
        <span class="front-logo__dot"></span>
      </div>
      <div class="front-logo__sub">Builders, Inc.</div>
    </div>
    <div class="band band--bottom"></div>
  </section>

  <section class="card card--back">
    <div class="band band--top"></div>
    <div class="back-art" role="img" aria-label="Illustration of three smiling roofing workers holding tools in front of a house"></div>
    <div class="back-info">
      <div class="back-info__brand">Fair Deal</div>
      <div class="back-info__brand-sub">Builders, Inc.</div>
      <div class="back-info__person">SAM PORTER</div>
      <div class="back-info__title">Keel Certified Roof Inspector</div>
      <div class="back-info__title">Licensed Property Adjuster</div>
      <ul class="contact-list">
        <li>(555) 014-2080
          <svg viewBox="0 0 24 24"><path d="M6.6 10.8a15 15 0 0 0 6.6 6.6l2.2-2.2c.3-.3.7-.4 1-.2 1.1.4 2.3.6 3.6.6.6 0 1 .4 1 1V20c0 .6-.4 1-1 1A17 17 0 0 1 3 4c0-.6.4-1 1-1h3.5c.6 0 1 .4 1 1 0 1.3.2 2.5.6 3.6.1.3 0 .7-.2 1z"/></svg></li>
        <li>(555) 014-7354
          <svg viewBox="0 0 24 24"><rect x="6" y="2" width="12" height="20" rx="2"/></svg></li>
        <li>sam@fairdealtx.com
          <svg viewBox="0 0 24 24"><path d="M2 5h20v14H2z M2 5l10 8 10-8" stroke="#3b211b" stroke-width="1.5"/></svg></li>
        <li class="no-icon">4410 Cedar Lane Suite 120</li>
        <li class="no-icon">Plano, TX 75093</li>
      </ul>
    </div>
    <div class="band band--bottom"></div>
  </section>
</body>
</html>
```